Redesign of a Brochure based on an exsiting example for Web download and email marketing

Can you create a professional brochure based on the attached PDF. We need to keep the name, the logo and the content but everything else can be changed . The PDF will primarily be will be used for web download and email marking but it aslo be printed out for a poster design will be appropriate

Target Market(s)

Business to Business

Industry/Entity Type

Marketing

Font styles to use
Serif

Requirements
Must have
• Must have the existing logo ( in the attached document) and contain the same content

```html
<!DOCTYPE html>
<html lang="en">
<head>
<meta charset="utf-8">
<title>Verantis – IT Run Model 1 Brochure</title>
<link href="https://fonts.googleapis.com/css2?family=Open+Sans:wght@300;400;600;700&family=Roboto+Condensed:wght@400;700&display=swap" rel="stylesheet">
<style>
  :root{
    --navy:#1c2473;
    --royal:#2b35a6;
    --ink:#1a1a1a;
    --paper:#f3f3f5;
    --mist:#d9dbe2;
    --bar:#222222;
    --stage:#e9e9eb;
    --white:#ffffff;
  }
  *{box-sizing:border-box;margin:0;padding:0}
  html,body{width:1200px;height:1200px;overflow:hidden;background:var(--stage);font-family:"Open Sans",sans-serif;color:var(--ink)}
  .spread{position:absolute;left:70px;top:230px;width:1060px;height:740px;display:flex;gap:20px}
  .page{position:relative;width:520px;height:740px;overflow:hidden;box-shadow:0 10px 30px rgba(0,0,0,.18)}
  .page-bg{position:absolute;inset:0;width:100%;height:100%}
  .wordmark{position:absolute;display:flex;align-items:center;gap:12px;font-family:"Open Sans",sans-serif;font-weight:400;letter-spacing:.3em;font-size:30px}
  .wordmark .mark-square{width:18px;height:18px;background:currentColor}
  /* left page */
  .inside{background:linear-gradient(160deg,#fafafb 0%,#e6e7ec 100%)}
  .inside .wordmark{left:130px;top:130px;color:var(--ink)}
  .model-ribbon{position:absolute;left:110px;top:190px;background:var(--navy);color:var(--white);font-family:"Roboto Condensed",sans-serif;font-weight:700;font-size:14px;padding:6px 26px;clip-path:polygon(4% 0,100% 0,96% 100%,0 100%)}
  .intro{position:absolute;left:40px;top:232px;width:440px;font-size:10.5px;line-height:1.35}
  .detail{position:absolute;left:40px;top:348px;width:215px;font-size:10.5px;line-height:1.3;text-align:justify}
  .pie-chart{position:absolute;left:268px;top:365px;width:245px;height:196px}
  .pie-chart text{font-family:"Open Sans",sans-serif;font-size:9px;fill:var(--ink)}
  .hex-photo{position:absolute;left:30px;top:565px;width:160px;height:140px;clip-path:polygon(25% 0,75% 0,100% 50%,75% 100%,25% 100%,0 50%);background:radial-gradient(circle at 45% 55%,#5fc3e8 0%,#1f5f8f 45%,#0d1d3a 100%)}
  .contact-block{position:absolute;right:60px;top:640px;text-align:right;color:var(--white);border-right:2px solid var(--white);padding-right:12px}
  .contact-block h3{font-size:17px;font-weight:600}
  .contact-block p{font-size:12px;line-height:1.3}
  /* right page */
  .cover{background:var(--paper)}
  .cover-photo{position:absolute;left:0;top:100px;width:520px;height:340px;background:linear-gradient(180deg,#c9d7e6 0%,#9fb9d4 45%,#5d86b5 100%)}
  .cover .wordmark{left:105px;top:52px;color:var(--white)}
  .cover-info{position:absolute;left:30px;top:455px;width:460px}
  .model-number{font-weight:700;font-size:24px;letter-spacing:.01em}
  .date-published{font-family:"Roboto Condensed",sans-serif;font-weight:700;font-size:31px;color:var(--navy);line-height:1.05}
  .author{font-weight:300;font-size:25px;text-align:center}
  .contact-lines{margin-top:14px;text-align:center;font-size:12px;font-weight:600;line-height:1.4}
  .footer-bar{position:absolute;left:0;bottom:0;width:100%;height:62px;background:var(--bar);color:var(--white);font-size:12.5px;font-weight:600;display:flex;align-items:center;justify-content:center}
</style>
</head>
<body>
<main class="spread">
  <section class="page inside">
    <svg class="page-bg" viewBox="0 0 520 740" aria-hidden="true">
      <polygon points="0,0 180,0 520,110 520,130" fill="var(--navy)"/>
      <polygon points="0,0 80,0 520,140 520,150" fill="var(--royal)"/>
      <polygon points="0,620 520,560 520,740 0,740" fill="var(--navy)"/>
      <polygon points="0,600 520,545 520,560 0,620" fill="var(--royal)"/>
    </svg>
    <div class="wordmark"><span class="mark-square"></span>VERANTIS</div>
    <div class="model-ribbon">MODEL NAME: IT RUN MODEL 1</div>
    <p class="intro">IT Run Model 1 is a simple IT costing model suitable for any industry. It is designed to support a sophisticated level of cost transparency across common IT technologies, towers and services with a minimum of effort. As a starting point this model is mainly focused on the IT costs that "run" the business. However, it can be extended to cover a detailed view of IT investments that "change" the business as well. In addition, it can be used as a starting point to manage demand by extending support for specific business processes.</p>
    <p class="detail">This model is a concrete implementation of the Technology Business Management (TBM) standard framework. TBM has three main views: a Finance View, an IT View and a Business view. This model implements these views through three simple layers: IT Cost centres, IT Technology Towers and Products &amp; Services. You can start by implementing just the IT Cost Centres to get some valuable insights before moving on to the IT Towers and Product/Services layers.</p>
    <svg class="pie-chart" viewBox="0 0 245 196" role="img" aria-label="Pie chart of IT run cost by technology tower">
      <g transform="translate(122,103)">
        <path d="M0,0 L-8.7,-49.2 A50,50 0 0 1 49.2,8.7 Z" fill="#e8262b"/>
        <path d="M0,0 L49.2,8.7 A50,50 0 0 1 -38.3,32.1 Z" fill="#3b9be0"/>
        <path d="M0,0 L-38.3,32.1 A50,50 0 0 1 -47,-17.1 Z" fill="#a85fe0"/>
        <path d="M0,0 L-47,-17.1 A50,50 0 0 1 -8.7,-49.2 Z" fill="#f5e21b"/>
      </g>
      <text x="80" y="14">Tech Towers (Run Build Manage)</text>
      <text x="130" y="26">Apps Maintenance</text>
      <text x="10" y="48">Datacentre &amp;</text>
      <text x="10" y="59">Servers</text>
      <text x="0" y="95">End User</text>
      <text x="0" y="106">Computing</text>
      <text x="182" y="110">Helpesk &amp;</text>
      <text x="182" y="121">Ops Bridge</text>
      <text x="182" y="142">Not</text>
      <text x="182" y="153">Allocated</text>
      <text x="60" y="176">Networks &amp; Telecoms</text>
    </svg>
    <div class="hex-photo" role="img" aria-label="Hand holding a glowing digital globe with network graphics"></div>
    <div class="contact-block">
      <h3>Contact Us</h3>
      <p>xxx-xxxx-xx: Phone No.</p>
      <p>www.company.com :Yor Website</p>
    </div>
  </section>

  <section class="page cover">
    <div class="cover-photo" role="img" aria-label="Business team around a meeting table using phones and tablets under a glowing cloud"></div>
    <svg class="page-bg" viewBox="0 0 520 740" aria-hidden="true">
      <polygon points="0,0 520,0 520,100 260,175 0,100" fill="var(--navy)"/>
      <polygon points="0,100 260,175 520,100 520,112 260,190 0,112" fill="#c3c6d2"/>
      <polygon points="0,440 520,440 520,460 0,445" fill="var(--navy)"/>
    </svg>
    <div class="wordmark"><span class="mark-square"></span>VERANTIS</div>
    <div class="cover-info">
      <p class="model-number">PUBLISHED MODEL NUMBER:100001</p>
      <p class="date-published">DATE PUBLISHED: 05 JUNE 2015</p>
      <p class="author">AUTHOR: VERANTIS</p>
      <div class="contact-lines">
        <p>Contact: rpatel@ashfordvale.co.uk</p>
        <p>Related models: IT Build Model 1 - 100002</p>
      </div>
    </div>
    <div class="footer-bar">For Technology Business Management (TBM) see itcostforum.org</div>
  </section>
</main>
</body>
</html>
```